Sorpresa para un amigo
Zielgruppe
Tito, un español simpático de 32 años
Aufgabenstellung
Hola, soy Torsten, uno de los fundadores de quelvento.
Tres semanas antes he llevado el Camino de Santiago en España en la bicicleta y tengo con esto Tito, un español muy simpático de modo conocido. Hemos llevado en común aproximadamente 700 kilómetros y hemos vivido mucho juntos.
Tito tiene el 2 de julio el cumpleaños y quisiera sorprenderlo. Por favor, una tarjeta de cumpleaños hermosa forma para él, tenemos un recuerdo hermoso de Camino.
Podéis usar una de las fotos de las colocaciones e incorporar quizá algunas nuestras citas el más con mucho gusto:
¡Tiempo mal!
¡El culo mal!
¡La rodilla mal!
¿Cómo lejos todavía hasta Santiago?
La tarjeta debe ser expedida como E-Mail

```html
<!DOCTYPE html>
<html lang="es">
<head>
<meta charset="utf-8">
<title>Feliz cumpleaños, Tito</title>
<link rel="stylesheet" href="https://fonts.googleapis.com/css2?family=Arimo:wght@400;700&family=Reenie+Beanie&display=swap">
<style>
  :root {
    --frame-blue: #1f4e9c;
    --paper: #ffffff;
    --paper-shade: #eef0f2;
    --ink: #3a3a3a;
    --ink-soft: #555555;
    --shell-cream: #f6efd6;
    --card-white: #ffffff;
    --card-shadow: rgba(0, 0, 0, 0.28);
    --sky: #c9d8e6;
    --field: #7f9a52;
    --stone: #8a6a45;
  }
  * { margin: 0; padding: 0; box-sizing: border-box; }
  html, body {
    width: 1200px; height: 1200px; overflow: hidden;
    background: var(--paper);
  }
  .card {
    position: relative;
    width: 1200px; height: 1200px;
    background: var(--frame-blue);
    padding: 24px;
    font-family: "Arimo", Arial, sans-serif;
  }
  .card-face {
    position: relative;
    width: 100%; height: 100%;
    overflow: hidden;
    background: radial-gradient(circle at 60% 35%, var(--paper) 55%, var(--paper-shade) 100%);
  }
  .shell-motif {
    position: absolute;
    left: -130px; top: 600px;
    width: 620px; height: 620px;
    border-radius: 50%;
    background: radial-gradient(circle, var(--shell-cream) 0%, rgba(246, 239, 214, 0.55) 45%, rgba(246, 239, 214, 0) 70%);
  }
  .route-mark {
    position: absolute;
    right: 52px; top: 112px;
    display: flex;
    align-items: center;
    gap: 12px;
    color: var(--ink-soft);
    font-size: 28px;
    font-weight: 400;
    line-height: 1;
  }
  .route-mark .dot {
    width: 18px; height: 18px;
    border-radius: 50%;
    background: var(--ink-soft);
  }
  .photo-card {
    position: absolute;
    background: var(--card-white);
    border-radius: 14px;
    box-shadow: 4px 6px 18px var(--card-shadow);
    padding: 27px;
  }
  .photo-card--back {
    left: 79px; top: 139px;
    width: 394px; height: 471px;
    transform: rotate(-11deg);
  }
  .photo-card--front {
    left: 195px; top: 127px;
    width: 603px; height: 459px;
    transform: rotate(2deg);
  }
  .photo { width: 100%; height: 100%; }
  .photo--tower {
    background: linear-gradient(90deg, var(--stone) 0%, #b49470 55%, #e8e6e0 80%);
  }
  .photo--riders {
    background: linear-gradient(180deg, var(--sky) 0%, #eef2f5 35%, #a7b37f 48%, var(--field) 75%, #b8a57a 100%);
  }
  .complaints {
    position: absolute;
    right: 38px; top: 352px;
    text-align: right;
    color: var(--ink);
    font-size: 29px;
    line-height: 38px;
  }
  .complaints b { font-weight: 700; }
  .handwritten-question {
    position: absolute;
    left: 186px; top: 700px;
    font-family: "Reenie Beanie", cursive;
    font-size: 58px;
    color: var(--ink);
    letter-spacing: 1px;
  }
  .greeting {
    position: absolute;
    left: 164px; top: 800px;
    color: var(--ink);
    font-size: 68px;
    font-weight: 400;
    line-height: 1;
  }
  .toast {
    position: absolute;
    left: 166px; top: 872px;
    color: var(--ink);
    font-size: 42px;
    line-height: 1;
  }
</style>
</head>
<body>
  <div class="card">
    <div class="card-face">
      <div class="shell-motif" role="img" aria-label="Faint pilgrim shell motif in cream"></div>

      <div class="route-mark">
        <span class="dot"></span>
        <span>ruta jacobea 2009</span>
      </div>

      <div class="photo-card photo-card--back">
        <div class="photo photo--tower" role="img" aria-label="Photo of a stone cathedral tower against a pale sky"></div>
      </div>
      <div class="photo-card photo-card--front">
        <div class="photo photo--riders" role="img" aria-label="Photo of two cyclists standing on a hill above green Castilian fields"></div>
      </div>

      <div class="complaints">
        <div><b>Tiempo?</b>...mal!</div>
        <div><b>El culo?</b>...mal!</div>
        <div><b>La rodilla?</b>...mal!</div>
      </div>

      <p class="handwritten-question">¿como lejos todavía hasta Santiago?</p>
      <h1 class="greeting">Feliz cumpleaños, Tito!!</h1>
      <p class="toast">Brindo por 700 km de amistad...</p>
    </div>
  </div>
</body>
</html>
```